New italian pizza restaurant in Australia, looking for a clean and crisp new take away leaflet de...

We require a leaflet for a take away menu / introduction to the area for our new italian pizza restaurant. AS we are a brand new business we need to get the word out about opening and specials as well as a takeaway menu. I have attached logo and menu items along with a basic design concept to help speed up the process.

Target Market(s)

Widest age range possible, families

Colors

Designer to choose colors to be used in the design.

```html
<!DOCTYPE html>
<html lang="en">
<head>
<meta charset="utf-8">
<title>Marlowe Pizzeria – Takeaway Menu</title>
<link rel="stylesheet" href="https://fonts.googleapis.com/css2?family=Source+Sans+3:wght@400;600;700&display=swap">
<style>
  :root{
    --page:#f2f2f0;
    --frame:#4a8f57;
    --ink:#0b0b0b;
    --orange:#f04e1f;
    --green:#3f8f55;
    --white:#ffffff;
    --slice:#6e2410;
  }
  *{box-sizing:border-box;margin:0;padding:0}
  html,body{width:1200px;height:931px;overflow:hidden;background:var(--page)}
  body{font-family:"Source Sans 3",sans-serif;color:var(--white)}
  .leaflet{position:absolute;left:19px;top:19px;width:1162px;height:895px;background:var(--ink);overflow:hidden}
  .band{position:absolute;left:0;width:100%;background:var(--frame);z-index:2}
  .band--top{top:0;height:21px}
  .band--bottom{bottom:0;height:17px}
  .panel{position:absolute;top:21px;bottom:17px}
  .panel--menu{left:0;width:372px;background:linear-gradient(180deg,#0a0a0a,#141414 60%,#0c0c0c)}
  .panel--pizza{left:372px;width:396px;background:linear-gradient(180deg,#0c0c0c,#161616 50%,#0b0b0b)}
  .panel--cover{left:768px;width:394px;background:#070707}
  .cover-glow{position:absolute;left:0;top:0;width:100%;height:534px;background:radial-gradient(ellipse at 50% 55%,#34383b 0%,#1d1f21 55%,#101112 100%)}

  .heading{color:var(--orange);font-weight:600;font-size:15.5px;line-height:16.5px}
  .abs{position:absolute}
  .item-name{font-size:12.5px;font-weight:700;line-height:13px}
  .item-name span{margin-left:10px}
  .item-desc{color:var(--green);font-size:11.7px;line-height:12px}
  .mains .item{height:27.8px}
  .salads .item{margin-bottom:7px}
  .pasta .item{height:29.8px}
  .pasta .item-name{font-weight:400}
  .small-head{color:var(--orange);font-weight:700;font-size:13px;line-height:12.5px}
  .small-list{color:var(--green);font-size:11.4px;line-height:11.8px}

  .pizza-title{left:0;width:100%;top:23px;text-align:center;font-size:21px;font-weight:600;color:var(--orange)}
  .slice{position:absolute;background:var(--slice);border-radius:6px;opacity:.85}
  .pizza{position:absolute;left:44px;width:352px;font-size:14.2px;line-height:15.4px}
  .pizza b{color:var(--orange);font-weight:600;font-size:17.5px}

  .brand{position:absolute;left:0;width:100%;top:217px;text-align:center;font-weight:700;color:var(--white)}
  .brand-dot{width:22px;height:22px;border-radius:50%;background:var(--orange);margin:0 auto 14px}
  .brand-name{font-size:38px;line-height:40px;letter-spacing:2px}
  .brand-sub{font-size:17px;line-height:22px;letter-spacing:8px;margin-top:8px}
  .address{position:absolute;left:0;width:100%;top:598px;text-align:center;color:var(--green);font-weight:700;font-size:21px;line-height:26px}
  .tel{position:absolute;left:0;width:100%;top:671px;text-align:center;color:var(--green);font-weight:700;font-size:18px}
  .tel strong{color:var(--orange);font-size:31px;margin-left:6px}
  .order{position:absolute;left:60px;top:749px;width:272px;height:44px;border:2px solid var(--green);border-radius:20px;text-align:center;font-weight:700;font-size:23px;line-height:40px}
  .order-arrow{position:absolute;left:325px;top:773px}
  .web{position:absolute;left:0;width:100%;top:800px;text-align:center;color:var(--orange);font-size:21px}
</style>
</head>
<body>
<div class="leaflet">
  <div class="band band--top"></div>

  <section class="panel panel--menu">
    <h2 class="heading abs" style="left:18px;top:9px">Main Meals (all mains served with chips or salad)</h2>
    <div class="mains abs" style="left:12px;top:42px;width:360px">
      <div class="item"><p class="item-name">Scotch Fillet Steak 300g<span>$25</span></p><p class="item-desc">grass fed, with your choice of Mushroom, Pepper or Garlic sauce</p></div>
      <div class="item"><p class="item-name">Calamari<span>$19.5</span></p><p class="item-desc">Flash fried or crumbed squid with aioli</p></div>
      <div class="item"><p class="item-name">Chicken Parmigiana<span>$19.5</span></p><p class="item-desc">Schnitzel topped with ham, Napoli sauce &amp; mozzarella</p></div>
      <div class="item"><p class="item-name">Veal Scallopini<span>$19.5</span></p><p class="item-desc">with your choice of mushroom or creamy avocado sauce</p></div>
      <div class="item"><p class="item-name">Veal Parmigiana<span>$19.5</span></p><p class="item-desc">schnitzel topped ham, Napoli sauce &amp; mozzarella</p></div>
    </div>

    <h2 class="heading abs" style="left:0;width:100%;top:196px;text-align:center">Salads</h2>
    <div class="salads abs" style="left:12px;top:228px;width:360px">
      <div class="item"><p class="item-name">Greek Salad<span>$14.5</span></p><p class="item-desc">cos lettuce, tomato, onion, cucumber, olives, feta cheese &amp; dressing</p></div>
      <div class="item"><p class="item-name">Grilled Chicken Salad<span>$15.5</span></p><p class="item-desc">Seasoned chicken, mixed leaves, cherry tomato, Spanish onion,<br>cucumber with garlic infused olive oil</p></div>
      <div class="item"><p class="item-name">Chicken Ceasar Salad<span>$15.5</span></p><p class="item-desc">Chicken, cos lettuce, croutons, shaved parmesan, anchovies, egg,<br>bacon served with ceaser dressing</p></div>
    </div>

    <h2 class="heading abs" style="left:0;width:100%;top:358px;text-align:center">Pasta- Spaghetti, Penne, Gnocchi, Fettucine,<br>Linguine</h2>
    <div class="pasta abs" style="left:12px;top:404px;width:360px">
      <div class="item"><p class="item-name">Bolognese<span>$14</span></p><p class="item-desc">traditional Italian meat sauce</p></div>
      <div class="item"><p class="item-name">Carbonara<span>$14</span></p><p class="item-desc">onion, bacon, egg in creamy parmesan cheese sauce</p></div>
      <div class="item"><p class="item-name">Napolitana<span>$13.5</span></p><p class="item-desc">traditional Italian Napoli sauce</p></div>
      <div class="item"><p class="item-name">Amatriciana<span>$15</span></p><p class="item-desc">bacon, onion, olives, capsicum, fresh chili cooked in Napoli sauce</p></div>
      <div class="item"><p class="item-name">Marinara<span>$15</span></p><p class="item-desc">mussels, prawns, calamari, scallops cooked in Napoli sauce</p></div>
      <div class="item"><p class="item-name">Risotto Polo<span>$16.5</span></p><p class="item-desc">chicken, mushroom, onion, cooked in a cream sauce</p></div>
      <div class="item"><p class="item-name">Lasagna<span>$15</span></p><p class="item-desc">Homemade Lasagna</p></div>
      <div class="item"><p class="item-name">Pasta Your way<span>$14.5</span></p><p class="item-desc">choose any three ingredients with cream or Napoli sauce</p></div>
    </div>

    <div class="abs" style="left:13px;top:656px">
      <p class="small-head">Kids Menu $9.5</p>
      <p class="small-list">Pasta Bolognese<br>Pasta Napoli<br>Chicken Nuggets &amp; Chips<br>Cheeseburger &amp; Chips</p>
    </div>
    <div class="abs" style="left:196px;top:656px">
      <p class="small-head">Sides</p>
      <p class="small-list">Garlic Bread $4.5<br>Chips $7.5<br>Garden Salad $5</p>
    </div>
    <div class="abs" style="left:13px;top:728px">
      <p class="small-head">Desserts</p>
      <p class="small-list">Gelati 500mls Varieties $6.5<br>Baci $6<br>Tartufo $6<br>Chocolate Mousse $6</p>
    </div>
    <div class="abs" style="left:196px;top:728px">
      <p class="small-head">Drinks</p>
      <p class="small-list">Soft drinks 375ml - $2.5<br>Soft drinks 1.25L - $4.5<br>Water 600ml - $2.5</p>
    </div>
    <div class="abs" style="left:13px;top:798px">
      <p class="small-head">Combo Deals</p>
      <p class="small-list">Any 2 Family pizzas, garlic bread and 1.25l soft drink - $41.00<br>1 Large pizza, 1 pasta, garlic bread and 1.25l soft drink - $38.00<br>2 Large pizzas, 1 garlic bread and 1.25l soft drink - $36.00</p>
    </div>
  </section>

  <section class="panel panel--pizza">
    <div class="slice" style="left:31px;top:1px;width:94px;height:66px" role="img" aria-label="Hand-drawn pizza slice illustration"></div>
    <div class="slice" style="left:252px;top:0;width:126px;height:64px" role="img" aria-label="Hand-drawn pizza slice illustration"></div>
    <h2 class="pizza-title abs">PIZZA</h2>

    <p class="pizza" style="top:81px"><b>Capricciosa</b> – tomato, cheese, ham,<br>mushrooms, olives Small $9 Large $15 Family $18</p>
    <p class="pizza" style="top:123px"><b>Napoli</b> – tomato, cheese, olives, anchovies $9 $15 $18</p>
    <p class="pizza" style="top:149px"><b>American</b> – tomato, cheese, salami $9 $15 $18</p>
    <p class="pizza" style="top:176px"><b>Vegetarian</b> – tomato, cheese, mushroom, onions,<br>capsicum, olives $9 $15 $18</p>
    <p class="pizza" style="top:217px"><b>Seafood</b> – tomato, cheese, prawns, clams, anchovies<br>$9.5 $15.5 $19</p>
    <p class="pizza" style="top:258px"><b>The Hot One</b> – tomato, cheese, ham, salami,<br>chilli $9 $15 $18</p>
    <p class="pizza" style="top:299px"><b>Margherita</b> – tomato, cheese, oregano $8.5 $14.5 $17</p>
    <p class="pizza" style="top:325px"><b>The Lot</b> – tomato, cheese, ham, salami, bacon,<br>mushroom, onions, capsicum, pineapple, olives $10 $16<br>$19</p>
    <p class="pizza" style="top:381px"><b>Mexican</b> – tomato, cheese, salami, capsicum, chilli $9<br>$15 $18</p>
    <p class="pizza" style="top:422px"><b>Chicken</b> – tomato, cheese, chicken, BBQ sauce $9 $15<br>$18</p>
    <p class="pizza" style="top:463px"><b>Meat Lovers</b> – tomato, cheese, ham, salami, bacon,<br>BBQ sauce $10 $16 $19</p>
    <p class="pizza" style="top:504px"><b>The House Pizza</b> – tomato, cheese, ham, mushroom,<br>capsicum $9 $15 $18</p>
    <p class="pizza" style="top:545px"><b>Ceaser’s Pizza</b> – tomato, cheese, ham, mushroom,<br>pineapple, prawns $10 $16 $19</p>
    <p class="pizza" style="top:587px"><b>The Breakie Pizza</b> – tomato, cheese, bacon, egg $9<br>$15 $18</p>
    <p class="pizza" style="top:628px"><b>The Footy Special</b> – tomato, cheese, ham,<br>capsicum, onions, pineapple $9 $15 $18</p>
    <p class="pizza" style="top:669px"><b>The Marlowe</b> – tomato, cheese ham, mushrooms,<br>onions, olives $9 $15 $18</p>
    <p class="pizza" style="top:710px"><b>The Marl Special</b> – tomato, cheese, ham, onions,<br>bacon, egg $10 $16 $19</p>
    <p class="pizza" style="top:750px;font-size:16px"><b>Ham</b> - tomato, cheese, ham $8.5 $14.5 $17</p>
    <p class="pizza" style="top:777px;font-size:16px"><b>Garlic</b> – garlic, cheese, oregano $8.5 $14.5 $17</p>
  </section>

  <section class="panel panel--cover">
    <div class="cover-glow"></div>
    <div class="brand">
      <div class="brand-dot"></div>
      <p class="brand-name">MARLOWE</p>
      <p class="brand-sub">PIZZERIA</p>
    </div>
    <p class="address">27 Kestrel Dr,<br>Brookvale 3048</p>
    <p class="tel">Tel:<strong>412 906 318</strong></p>
    <div class="order">ORDER ONLINE :</div>
    <svg class="order-arrow" width="20" height="24" viewBox="0 0 20 24" aria-hidden="true">
      <path d="M1 1 L19 11 L11 12 L16 22 L13 23 L8 14 L2 18 Z" fill="var(--green)"/>
    </svg>
    <p class="web">www.marlowepizza.au</p>
  </section>

  <div class="band band--bottom"></div>
</div>
</body>
</html>
```